依頼詳細
ヘーゼルナッツ70g入りの透明なスタンドパックに印刷ではなくシール対応で簡素なデザインを施したいと思います。基本的には風袋の裏面には輸入者表示、表面にシールを貼るという前提ですが、勿論デザイナーの方からのご提案も喜んで受けたいと思います。
記載項目
パッケージのサイズについては下記を参考になさって下さい、商品名はQT-4 後ほど商品を入れた状態での画像を添付します。

https://www.582pack.co.jp/item_info/07-3300-58200/?ref=Xm4TqWz8LbR2vNcP7sKdE3yHfJ9aG5uQ1oVtB6rZnM0wLxCeY8pDkS4hTgA2jF7qU9iOl3WbN5mRvK1zXc
希望イメージ
シンプル 複雑
単色 カラフル
暗い 明るい
日常 高級
遊び心 厳粛
未来的 伝統的
女性的 男性的
希望する色
緑系
納品ファイル
• 高解像度JPG (.jpg)
補足説明
可能であればシール自体の素材も剥がしやすい物を選び、結果的にごみ分別の際にも環境に優しい、いわゆるエコな方向性を目指しています。
どうやら米国外からの閲覧が一部制限されているようです。下記のサイトなら米国で販売されている小売商品が拝見出来ます。

https://www.tamsingrove.com/
業務用に900g入りのスタンドパックも販売予定です。
QT-4 に実際にヘーゼルナッツを入れた状態で撮影しました。下手糞な素人写真ですがなんとなく雰囲気だけは判るかと。
このコピー、With Love From Oregon を何らかの形でデザインに組み込んでもらえると嬉しいです。
皆様 ご提案ありがとうございます。残念ながらTamsin Grove のロゴは今回は許可が下りませんでしたので使えません。それから英語の表記について、Dry Roasted Whole ではなく、 Dry Roasted 又は Dry Roasted Unsalted に最終的にはなると思います。どうかよろしくお願い致します。
英語の表記はこの際 HAZELNUTS に統一したいと思います。以上、よろしくお願い致します。
■ 選んだ理由

素朴さと親しみやすさを兼ね備えたデザインだと思います。又、こちらの我儘なリクエストにも迅速且つ的確に対応して頂きました。改めましてこの度はありがとうございました!

■ 提案者全員のお礼・コメント

多くの応募を頂き嬉しい限りです。今回は日本語を中心としたデザインでしたが、近日中に第二弾として、全く日本語の入らないパッケージデザイン(このまま米国の市場でも販売可能な)を検討しています。この際には今回応募頂いた方々にも是非再度参加して頂ければ幸いです。どうかよろしくお願い致します。

```html
<!DOCTYPE html>
<html lang="en">
<head>
<meta charset="utf-8">
<title>Tamsin Grove Hazelnuts – Label TypeB2</title>
<link rel="stylesheet" href="https://fonts.googleapis.com/css2?family=Anton&family=Oswald:wght@500;600&family=Bitter:wght@700&family=Roboto+Condensed:wght@700&family=Source+Sans+3:wght@400&display=swap">
<style>
  :root {
    --page: #ffffff;
    --cream: #f3efe6;
    --brand-green: #4d6b2a;
    --nut-brown: #3d2a1d;
    --roast-orange: #c06a32;
    --band-green: #8db52a;
    --leaf-light: #a8b45a;
    --leaf-dark: #55662a;
    --nut-light: #c9bfb3;
    --nut-dark: #8a6a52;
    --badge-green: #5aa02c;
    --sticker-red: #d8232f;
    --ink: #222222;
  }
  * { margin: 0; padding: 0; box-sizing: border-box; }
  html, body { width: 943px; height: 1200px; overflow: hidden; background: var(--page); }
  .canvas { position: relative; width: 943px; height: 1200px; }
  .variant-tag {
    position: absolute; top: 64px; right: 8px;
    font: 400 22px/1 "Source Sans 3", sans-serif; color: var(--ink);
  }
  .label {
    position: absolute; left: 353px; top: 197px; width: 229px; height: 254px;
    background: var(--cream); overflow: hidden;
  }
  .brand {
    height: 61px; display: flex; align-items: center; justify-content: center;
    font: 700 24px/1 "Bitter", serif; color: var(--brand-green);
  }
  .photos { position: relative; height: 96px; display: flex; }
  .photo-orchard {
    width: 84px; height: 100%;
    background: linear-gradient(150deg, var(--leaf-light), var(--leaf-dark));
  }
  .photo-nuts {
    flex: 1; height: 100%;
    background: radial-gradient(circle at 60% 40%, var(--nut-light), var(--nut-dark));
  }
  .claim-badge {
    position: absolute; left: 3px; top: 56px; width: 54px; height: 38px;
    background: var(--badge-green); color: #fff; text-align: center;
    font-family: "Oswald", sans-serif; line-height: 1;
    padding-top: 4px;
  }
  .claim-badge .claim-top { font-size: 8px; font-weight: 600; display: block; }
  .claim-badge .claim-num { font-size: 13px; font-weight: 600; display: block; }
  .claim-badge .claim-note { font-size: 4px; display: block; letter-spacing: .2px; }
  .love-sticker {
    position: absolute; right: 6px; top: 70px; width: 40px; height: 40px;
    border-radius: 50%; background: var(--sticker-red);
  }
  .product-name {
    margin-top: 9px; text-align: center;
    font: 400 38px/1 "Anton", sans-serif; color: var(--nut-brown); letter-spacing: 1px;
  }
  .product-style {
    margin-top: 5px; display: flex; align-items: center; justify-content: center; gap: 4px;
    font: 500 18px/1 "Oswald", sans-serif; color: var(--roast-orange);
  }
  .product-style .rule { width: 8px; height: 5px; border-top: 1px solid var(--roast-orange); border-bottom: 1px solid var(--roast-orange); }
  .net-weight {
    position: absolute; left: 0; bottom: 0; width: 100%; height: 14px;
    background: var(--band-green); color: #fff; text-align: center;
    font: 700 7px/14px "Roboto Condensed", sans-serif;
  }
</style>
</head>
<body>
<div class="canvas">
  <div class="variant-tag">TypeB2</div>

  <section class="label">
    <div class="brand">Tamsin Grove</div>

    <div class="photos">
      <div class="photo-orchard" role="img" aria-label="Photo of hazelnuts growing among green orchard leaves"></div>
      <div class="photo-nuts" role="img" aria-label="Photo of roasted whole hazelnuts scattered on a table"></div>
      <div class="claim-badge">
        <span class="claim-top">GROWS</span>
        <span class="claim-num">99%</span>
        <span class="claim-note">OF US HAZELNUTS</span>
      </div>
      <div class="love-sticker" role="img" aria-label="Red sticker with the slogan With Love from Oregon"></div>
    </div>

    <h1 class="product-name">HAZELNUTS</h1>
    <p class="product-style"><span class="rule"></span>DRY ROASTED WHOLE<span class="rule"></span></p>
    <div class="net-weight">NET WT 70g</div>
  </section>
</div>
</body>
</html>
```